New Business Card Design Project

I have a logo I would like to use on the business card. I want something that will stand out and that will be remembered.

Target Market(s)

People who collect gems, minerals and crystals.

Contact Information for Business Card

email - mkthestonefalcon@vendrollo.com
phone # 917-406-2581

Font styles to use
Serif
Sans Serif
Decorative

Colors

Designer to choose colors to be used in the design.

Requirements
Must have
• The logo...two to choose from.
Nice to have
• An eye catching and memorable way to draw in people who collect gems minerals and crystals.

```html
<!DOCTYPE html>
<html lang="en">
<head>
<meta charset="utf-8">
<title>The Stone Falcon — Business Card</title>
<link href="https://fonts.googleapis.com/css2?family=Work+Sans:wght@400;500;700&display=swap" rel="stylesheet">
<style>
  :root {
    --stage: #1c1c1c;
    --card: #1e1e1f;
    --card-edge: #2a2a2b;
    --ink: #ffffff;
    --accent-bright: #3a4fd6;
  }
  * { margin: 0; padding: 0; box-sizing: border-box; }
  html, body {
    width: 1200px; height: 900px; overflow: hidden;
    background: var(--stage);
    font-family: "Work Sans", Arial, sans-serif;
  }
  .canvas {
    width: 1200px; height: 900px;
    display: flex; flex-direction: column;
    align-items: center; justify-content: center; gap: 40px;
  }
  .card {
    position: relative;
    width: 680px; height: 388px;
    background: var(--card);
    border: 1px solid var(--card-edge);
    box-shadow: 0 18px 40px rgba(0,0,0,.55);
    overflow: hidden;
  }
  /* Brand block, shared by both sides */
  .brand {
    display: flex; align-items: center; gap: 14px;
    color: var(--ink);
    font-weight: 700; text-transform: uppercase;
    letter-spacing: 1px; line-height: 1.05;
  }
  .brand__dot {
    width: 20px; height: 20px; border-radius: 50%;
    background: var(--accent-bright); flex: none;
  }
  .brand__name { display: block; }
  /* Front */
  .card--front { display: flex; align-items: center; justify-content: center; }
  .card--front .brand { font-size: 32px; }
  /* Back */
  .person { position: absolute; left: 48px; top: 40px; }
  .person__name {
    color: var(--accent-bright);
    font-weight: 500; font-size: 26px; letter-spacing: 2px; text-transform: uppercase;
  }
  .person__role { color: var(--ink); font-size: 15px; margin-top: 2px; }
  .address {
    position: absolute; left: 48px; top: 150px;
    color: var(--ink); font-size: 17px; line-height: 1.5; letter-spacing: .5px;
  }
  .contact {
    position: absolute; left: 48px; top: 262px;
    list-style: none; color: var(--ink); font-size: 16px; letter-spacing: .3px;
  }
  .contact li { display: flex; align-items: center; gap: 10px; line-height: 1.6; white-space: nowrap; }
  .contact svg { width: 12px; height: 12px; flex: none; }
  .contact .accent { color: var(--accent-bright); }
  .card--back .brand {
    position: absolute; right: 44px; top: 150px;
    font-size: 40px; text-align: right;
  }
</style>
</head>
<body>
  <main class="canvas">
    <section class="card card--front" aria-label="Card front">
      <div class="brand"><span class="brand__dot"></span><span class="brand__name">The Stone Falcon</span></div>
    </section>

    <section class="card card--back" aria-label="Card back">
      <div class="person">
        <h1 class="person__name">Marla Kendrick</h1>
        <p class="person__role">Director</p>
      </div>
      <p class="address">42b Harlow Lane,<br>Westbury, NZ, 7304</p>
      <ul class="contact">
        <li>
          <svg viewBox="0 0 12 12" aria-hidden="true"><path d="M3 1 L5 3.5 L4 5 Q5 7.5 7 8 L8.5 7 L11 9 L9.5 11 Q3 10 1 2.5 Z" fill="var(--accent-bright)"/></svg>
          917-406-2581
        </li>
        <li>
          <svg viewBox="0 0 12 12" aria-hidden="true"><rect x="1" y="2.5" width="10" height="7" fill="none" stroke="var(--accent-bright)" stroke-width="1.2"/><path d="M1 2.5 L6 6.5 L11 2.5" fill="none" stroke="var(--accent-bright)" stroke-width="1.2"/></svg>
          mkthestonefalcon@vendrollo.com
        </li>
        <li>
          <svg viewBox="0 0 12 12" aria-hidden="true"><circle cx="6" cy="6" r="5" fill="none" stroke="var(--accent-bright)" stroke-width="1.2"/><ellipse cx="6" cy="6" rx="2.2" ry="5" fill="none" stroke="var(--accent-bright)" stroke-width="1"/><path d="M1 6 H11" stroke="var(--accent-bright)" stroke-width="1"/></svg>
          <span>www.<span class="accent">mkthestonefalcon</span>.com</span>
        </li>
      </ul>
      <div class="brand"><span class="brand__dot"></span><span class="brand__name">The Stone<br>Falcon</span></div>
    </section>
  </main>
</body>
</html>
```